Copperfield Hide Renewal Product Label

We need a design for a label to be used on bottles of leather cleaner and conditioner products that will be used in curated kits. We would like it to incorporate our business logo as well as have an area that we can fill in later with the appropriate product name as needed. We would like to see designs that use shades of brown, but we are open to other colors often seen in leather. I am including the Copperfield Hide business Logo below, however again we would prefer to have the label in various shades of browns, rather than the red and grey, more like the mock-up that I am also attaching.

*** I am attaching examples of the types of bottles that will be used. They vary in size from 8 oz to 16 oz. if you are designing a label for a spray bottle they are from 16-32 oz. ***

```html
<!DOCTYPE html>
<html lang="en">
<head>
<meta charset="utf-8">
<title>Copperfield Hide Renewal – Product Labels</title>
<link rel="stylesheet" href="https://fonts.googleapis.com/css2?family=Arvo:wght@700&family=Arimo:wght@400;700&display=swap">
<style>
  :root {
    --page: #ffffff;
    --copper-dark: #2a1712;
    --copper-mid: #6b3b2c;
    --copper-light: #8a4b3a;
    --leather-dark: #1f1210;
    --leather-mid: #3a211a;
    --gold: #d9c48f;
    --gold-deep: #b89d5c;
    --silver-light: #f2f2f2;
    --silver-mid: #b9b9b9;
    --silver-dark: #6d6d6d;
    --stitch: #d8cfc4;
    --body-text: #e6ddd2;
    --tag-text: #1e1e1e;
  }
  * { box-sizing: border-box; margin: 0; padding: 0; }
  html, body { width: 1200px; height: 900px; overflow: hidden; background: var(--page); }
  .stage { position: relative; width: 1200px; height: 900px; }

  .label {
    position: absolute;
    border-radius: 34px;
    overflow: hidden;
    background: linear-gradient(180deg, var(--leather-mid), var(--leather-dark));
    display: flex; flex-direction: column;
  }
  .label--cleaner { left: 230px; top: 170px; width: 410px; height: 560px; }
  .label--conditioner { left: 690px; top: 200px; width: 290px; height: 500px; border-radius: 26px; }

  .label__brand-band {
    flex: 0 0 auto;
    height: 108px;
    background: linear-gradient(90deg, var(--copper-dark) 0%, var(--copper-mid) 30%, var(--copper-light) 70%, var(--copper-mid) 100%);
    display: flex; align-items: center; justify-content: center; gap: 10px;
  }
  .label--conditioner .label__brand-band { height: 110px; }
  .brand__dot {
    width: 34px; height: 34px; border-radius: 50%;
    background: var(--gold); flex: 0 0 auto;
  }
  .label--conditioner .brand__dot { width: 28px; height: 28px; }
  .brand__name {
    font-family: "Arimo", sans-serif; font-weight: 400;
    color: var(--gold); font-size: 19px; letter-spacing: 0.04em;
    text-transform: uppercase; line-height: 1.1; text-align: left;
  }
  .label--conditioner .brand__name { font-size: 14px; }

  .label__chrome-bar {
    flex: 0 0 auto; height: 14px;
    background: linear-gradient(90deg, var(--silver-dark), var(--silver-light) 25%, var(--silver-mid) 50%, var(--silver-light) 75%, var(--silver-dark));
  }

  .label__panel { position: relative; flex: 1 1 auto; }
  .label__stitch {
    position: absolute; inset: 12px;
    border: 1.5px dashed var(--stitch);
    border-radius: 30px;
    display: flex; flex-direction: column; align-items: center;
    padding: 52px 20px 20px;
  }
  .label--conditioner .label__stitch { inset: 10px; border-radius: 22px; padding-top: 46px; }

  .product-title {
    font-family: "Arvo", serif; font-weight: 700;
    color: var(--gold); text-align: center;
    font-size: 44px; line-height: 1.02; letter-spacing: 0.01em;
    text-shadow: 0 2px 2px rgba(0,0,0,0.5);
  }
  .label--conditioner .product-title { font-size: 34px; }
  .label--conditioner .product-title .product-title__line--long { font-size: 27px; }

  .product-tag {
    margin-top: 14px;
    padding: 5px 12px;
    border-radius: 4px;
    border: 1px solid var(--silver-dark);
    background: linear-gradient(180deg, var(--silver-light), var(--silver-mid));
    font-family: "Arimo", sans-serif; font-weight: 700;
    font-size: 12px; color: var(--tag-text); letter-spacing: 0.03em;
  }
  .label--conditioner .product-tag { font-size: 10px; padding: 4px 8px; }

  .product-copy {
    margin-top: auto;
    width: 86%;
    border-top: 1px solid var(--body-text);
    padding-top: 6px;
    font-family: "Arimo", sans-serif; font-size: 11.5px; line-height: 1.12;
    color: var(--body-text); text-align: center;
  }
  .label--conditioner .product-copy { font-size: 9px; width: 90%; }
  .product-size {
    margin-top: 28px; margin-bottom: 8px;
    font-family: "Arimo", sans-serif; font-weight: 700;
    font-size: 11px; color: var(--body-text);
  }
  .label--conditioner .product-size { margin-top: 22px; font-size: 9px; }
</style>
</head>
<body>
<main class="stage">

  <section class="label label--cleaner" aria-label="Leather cleaner label">
    <header class="label__brand-band">
      <span class="brand__dot"></span>
      <span class="brand__name">Copperfield Hide<br>Renewal</span>
    </header>
    <div class="label__chrome-bar"></div>
    <div class="label__panel">
      <div class="label__stitch">
        <h1 class="product-title">LEATHER<br>CLEANER</h1>
        <p class="product-tag">SUPERIOR CLEANER</p>
        <p class="product-copy">Lorem ipsum dolor sit amet, consectetur cing elit, sed do eiusmod tempor incididunt ut labore et dolore magna aliqua. Quis ipsum su spendisse ultrices gravida.</p>
        <p class="product-size">16oz</p>
      </div>
    </div>
  </section>

  <section class="label label--conditioner" aria-label="Leather conditioner label">
    <header class="label__brand-band">
      <span class="brand__dot"></span>
      <span class="brand__name">Copperfield Hide<br>Renewal</span>
    </header>
    <div class="label__chrome-bar"></div>
    <div class="label__panel">
      <div class="label__stitch">
        <h1 class="product-title">LEATHER<br><span class="product-title__line--long">CONDITIONER</span></h1>
        <p class="product-tag">SUPERIOR CONDITIONER</p>
        <p class="product-copy">Lorem ipsum dolor sit amet, consectetur cing elit, sed do eiusmod tempor incididunt ut labore et dolore magna aliqua. Quis ipsum su spendisse ultrices gravida.</p>
        <p class="product-size">8oz</p>
      </div>
    </div>
  </section>

</main>
</body>
</html>
```